We are looking for a clean new looking business card.

We would like a new, clean, and modern type business card with our updated contact information. We are a small a plumbing and heating and gasfitting company who offer 24 hr emergency service as well.
We feel our logo looks best on a white background.
Our current cards are outdated, both the design and the information.

Industry/Entity Type

Plumbing and heating

Contact Information for Business Card

Logo, Name, Title, Phone#, Email, Website, "24/7 Emergency Service"

Colors
0054AA
0677BA
7BADD7
CADEEF
E8F1F8

```html
<!DOCTYPE html>
<html lang="en">
<head>
<meta charset="UTF-8">
<title>Clearwater Business Card</title>
<link rel="stylesheet" href="https://fonts.googleapis.com/css2?family=Poppins:wght@400;600;700&family=Bebas+Neue&display=swap">
<style>
  :root {
    --stage: #1c1c1c;
    --white: #ffffff;
    --ink: #2a2a2a;
    --blue-deep: #0054AA;
    --blue: #0677BA;
    --blue-mid: #4aa6d4;
    --blue-soft: #7BADD7;
    --blue-pale: #CADEEF;
    --blue-mist: #E8F1F8;
    --card-dark: #333333;
    --card-dark-tone: #3d3d3d;
  }
  * { box-sizing: border-box; margin: 0; padding: 0; }
  html, body { width: 1200px; height: 1015px; overflow: hidden; }
  body {
    background: var(--stage);
    font-family: "Poppins", sans-serif;
    position: relative;
  }
  .card {
    position: absolute;
    width: 620px;
    height: 354px;
    box-shadow: 0 14px 30px rgba(0,0,0,.55);
  }
  /* Front */
  .card-front {
    left: 80px; top: 90px;
    background: var(--white);
    color: var(--ink);
  }
  .brand {
    position: absolute; left: 44px; top: 96px;
    width: 250px;
  }
  .brand-name {
    font-weight: 700;
    font-size: 30px;
    letter-spacing: 2px;
    color: var(--blue);
    line-height: 1;
    display: flex; align-items: center; gap: 8px;
    white-space: nowrap;
  }
  .brand-dot {
    width: 14px; height: 14px; border-radius: 50%;
    background: var(--blue);
    flex: none;
  }
  .brand-tagline {
    margin-top: 8px;
    font-size: 8px;
    letter-spacing: 2.6px;
    font-weight: 600;
    color: var(--ink);
    white-space: nowrap;
  }
  .person { position: absolute; left: 44px; top: 176px; }
  .person-name { font-size: 24px; font-weight: 700; line-height: 1.1; }
  .person-first { color: var(--blue); }
  .person-title { font-size: 16px; margin-top: 2px; }
  .contacts { position: absolute; left: 44px; top: 250px; list-style: none; }
  .contacts li {
    display: flex; align-items: center; gap: 10px;
    font-size: 16px; line-height: 26px;
    white-space: nowrap;
  }
  .contacts svg { width: 16px; height: 16px; flex: none; }
  .web-accent { color: var(--blue); }
  .mark-area {
    position: absolute; right: 30px; top: 30px;
    width: 260px; height: 294px;
    border-radius: 40px;
    background: linear-gradient(160deg, var(--blue-deep) 0%, var(--blue) 35%, var(--blue-mid) 60%, var(--blue-soft) 85%, var(--blue-pale) 100%);
  }
  /* Back */
  .card-back {
    left: 500px; top: 590px;
    background: var(--card-dark);
  }
  .back-pattern {
    position: absolute; inset: 0;
    background: linear-gradient(135deg, var(--card-dark) 0%, var(--card-dark-tone) 100%);
  }
  .back-brand {
    position: absolute; left: 0; right: 0; top: 140px;
    text-align: center;
    font-weight: 700; font-size: 26px; letter-spacing: 3px;
    color: var(--blue-mid);
  }
  .back-slogan {
    position: absolute; left: 40px; bottom: 34px;
    font-family: "Bebas Neue", sans-serif;
    font-size: 40px; letter-spacing: 1px;
    color: var(--blue);
  }
</style>
</head>
<body>
  <section class="card card-front">
    <div class="brand">
      <div class="brand-name"><span class="brand-dot"></span><span>clearwater</span></div>
      <div class="brand-tagline">PLUMBING · HEATING · GASFITTING</div>
    </div>
    <div class="person">
      <div class="person-name"><span class="person-first">Daniel</span> Hart</div>
      <div class="person-title">Managing Director</div>
    </div>
    <ul class="contacts">
      <li>
        <svg viewBox="0 0 16 16" aria-hidden="true"><path fill="var(--blue)" d="M3.5 1.5l2.5 0 1 3.5-1.6 1.2a8 8 0 0 0 4.4 4.4L11 9l3.5 1v2.5c0 1-1 2-2 2C6.6 14.5 1.5 9.4 1.5 3.5c0-1 1-2 2-2z"/></svg>
        <span>044-987 654 321</span>
      </li>
      <li>
        <svg viewBox="0 0 16 16" aria-hidden="true"><rect x="1" y="3" width="14" height="10" fill="var(--blue)"/><path d="M1 3l7 6 7-6" fill="none" stroke="#fff" stroke-width="1.2"/></svg>
        <span>info@clearwaterpro.com</span>
      </li>
      <li>
        <svg viewBox="0 0 16 16" aria-hidden="true"><circle cx="8" cy="8" r="6.5" fill="none" stroke="var(--blue)" stroke-width="1.5"/><ellipse cx="8" cy="8" rx="3" ry="6.5" fill="none" stroke="var(--blue)" stroke-width="1.2"/><path d="M1.5 8h13" stroke="var(--blue)" stroke-width="1.2"/></svg>
        <span>www.<span class="web-accent">clearwaterpro</span>.com</span>
      </li>
    </ul>
    <div class="mark-area" role="img" aria-label="Large brand symbol in graded blues"></div>
  </section>

  <section class="card card-back">
    <div class="back-pattern" role="img" aria-label="Repeating brand symbol pattern in dark grey"></div>
    <div class="back-brand">clearwater</div>
    <div class="back-slogan">24/7 Emergency Services</div>
  </section>
</body>
</html>
```